redesign corporate website (software courses)

We need a complete redesign of the current website: http://t-o-m.example/ (training: http://t-o-m.example/pt-br/treinamento/web ); more clear, different color, navigation, header, footer, whatever (side note: site will be based on bootstrap and drupal). Most important pages:

http://t-o-m.example/pt-br/treinamento (trainingoverviewpage)
http://t-o-m.example/ (frontpage)
http://t-o-m.example/pt-br/treinamento/web (trianingdetailpage)

The design should be valid for further content pages (like http://t-o-m.example/pt-br/desenvolvimentodesoftware) and pages with forms (http://t-o-m.example/pt-br/contact or http://t-o-m.example/pt-br/training/web/register)

Logo attached in white and black and black with shadow.

Some other examples of training sites (just content examples - not as template for similar layout):

http://www.brivatutor.example/packages/4817/Website-Development-Professional-training.html?advid=12&gclid=XQa93kLpr42DFbvn3BqeWTZBqk
http://www.kodewerk-kurse.example/
http://www.lumacod.example/cursos/quill-framework-ii/
http://www.travert-academy.example/lp/php-development-training.aspx?gclid=ZM3rhuPqx51DGTRR8Bpeyk9B2B

Industry/Entity Type

Software

```html
<!DOCTYPE html>
<html lang="en">
<head>
<meta charset="utf-8">
<title>TOM Institute – Training</title>
<link href="https://fonts.googleapis.com/css2?family=Roboto:wght@300;400;500;700&display=swap" rel="stylesheet">
<style>
:root{
  --orange:#f25a16;
  --orange-dark:#e04f0f;
  --ink:#1e1e1e;
  --text:#444;
  --muted:#777;
  --band:#f2f2f2;
  --line:#dcdcdc;
  --white:#fff;
}
*{box-sizing:border-box;margin:0;padding:0}
html,body{width:843px;height:1200px;overflow:hidden;background:var(--white)}
body{position:relative;font-family:'Roboto',Arial,sans-serif;color:var(--text)}
.abs{position:absolute}

/* header */
.topline{left:0;top:0;width:843px;height:3px;background:var(--orange)}
.header{left:0;top:3px;width:843px;height:67px;background:var(--white)}
.brand{left:78px;top:19px;display:flex;align-items:center;gap:8px}
.brand-dot{width:30px;height:30px;border-radius:50%;background:var(--orange)}
.brand-name{font-size:24px;font-weight:700;color:var(--ink);letter-spacing:.5px}
.nav{top:30px;font-size:10.5px;color:var(--ink);letter-spacing:.3px}
.nav.active{color:var(--orange)}
.search{left:634px;top:28px;width:130px;height:16px;border:1px solid var(--line);background:#fafafa;font-size:7px;color:#999;padding:3px 5px}

/* hero */
.hero{left:0;top:70px;width:843px;height:348px;background:linear-gradient(100deg,#c7c2b4 0%,#e9e3c8 30%,#f2e9a8 50%,#d8d2c4 72%,#b9a7b2 100%)}
.hero-panel{left:85px;top:214px;width:365px;height:184px;background:rgba(255,255,255,.35)}
.hero-title{left:95px;top:224px;font-size:29px;font-weight:700;color:var(--ink)}
.ribbon{left:85px;width:350px;height:26px;background:var(--orange);clip-path:polygon(0 0,100% 0,94% 100%,0 100%);display:flex;align-items:center;padding-left:10px;gap:8px;color:var(--white);font-size:14px}
.ribbon i{width:14px;height:14px;border-radius:50%;background:var(--white);display:block;flex:none}

.enquire{left:593px;top:148px;width:157px;height:250px;background:rgba(255,255,255,.45)}
.enquire-head{left:593px;top:148px;width:157px;height:45px;background:var(--orange);color:var(--white);font-size:16px;font-weight:700;line-height:19px;padding:5px 14px}
.field{left:601px;width:141px;background:var(--white);border:1px solid var(--line);font-size:7px;color:#666;padding:5px 9px}
.captcha{left:665px;top:350px;width:55px;height:16px;background:#cfe3cf;font-size:11px;font-weight:500;color:#333;padding-left:6px;line-height:16px}
.btn{background:var(--orange);color:var(--white);font-size:8px;text-align:center;line-height:16px;height:16px}

/* intro */
.intro-bar{top:452px;width:4px;height:122px;background:var(--orange)}
.h2{font-size:17.5px;color:var(--ink);font-weight:400}
.para{font-size:7px;line-height:12px;color:var(--text);width:322px}

/* band */
.band{left:0;top:592px;width:843px;height:278px;background:var(--band)}
.what-item{left:78px;width:330px;height:44px;background:var(--white);display:flex}
.what-plus{width:25px;height:44px;background:var(--orange);color:var(--white);font-size:24px;font-weight:300;text-align:center;line-height:42px}
.what-text{font-size:7px;line-height:9px;padding:8px 10px 0 16px;color:var(--text)}
.serv-icon{width:58px;height:58px;border-radius:50%;background:var(--white);border:1px solid #e3e3e3}
.serv-title{font-size:7px;font-weight:700;color:var(--ink)}
.serv-text{font-size:7px;line-height:9px;color:var(--text);width:272px}

/* contact */
.contact-line{left:102px;font-size:10.5px;color:var(--ink)}
.contact-line.link{color:var(--orange)}
.quote-circle{left:373px;top:883px;width:102px;height:102px;border-radius:50%;background:var(--orange)}
.quote-mark{left:383px;top:906px;font-size:52px;font-weight:700;color:var(--white);line-height:1}
.portrait{left:430px;top:884px;width:100px;height:100px;border-radius:50%;background:radial-gradient(circle at 50% 40%,#e0c2aa,#b8a49a 60%,#f0eeea);border:3px solid var(--white)}
.testi{left:542px;top:910px;width:220px;font-size:7px;line-height:9px;color:var(--text)}
.testi-name{left:542px;top:973px;font-size:8px;font-weight:700;color:var(--ink)}

/* footer */
.footer{left:0;top:1016px;width:843px;height:184px;background:var(--orange);color:var(--white);text-align:center}
.footer h3{position:absolute;left:0;width:843px;top:29px;font-size:17.5px;font-weight:700}
.footer p{position:absolute;left:0;width:843px;top:50px;font-size:8px;line-height:10px}
.socials{position:absolute;left:384px;top:84px;display:flex;gap:9px}
.socials span{width:14px;height:14px;border-radius:50%;background:var(--white);display:block}
.fnav{position:absolute;left:0;width:843px;top:106px;font-size:9.5px;word-spacing:0}
.fnav span{margin:0 7px}
.fbrand{position:absolute;left:360px;top:134px;display:flex;align-items:center;gap:7px}
.fbrand .brand-dot{background:var(--white);width:22px;height:22px}
.fbrand .brand-name{color:var(--white);font-size:17px}
</style>
</head>
<body>

<div class="abs topline"></div>
<header class="abs header"></header>
<div class="abs brand"><span class="brand-dot"></span><span class="brand-name">TOM Institute</span></div>
<span class="abs nav active" style="left:372px">HOME</span>
<span class="abs nav" style="left:426px">TRAINING</span>
<span class="abs nav" style="left:497px">SERVICING</span>
<span class="abs nav" style="left:572px">CONTACT</span>
<div class="abs search">Enter your search...</div>

<div class="abs hero" role="img" aria-label="Photo of a smiling student with glasses in a bright computer classroom"></div>
<div class="abs hero-panel"></div>
<div class="abs hero-title">Learn web development</div>
<div class="abs ribbon" style="top:266px"><i></i>Lorem ipsum dolor sit amet, consectetur adipisci</div>
<div class="abs ribbon" style="top:299px"><i></i>Lorem ipsum dolor sit amet, consectetur adipisci</div>
<div class="abs ribbon" style="top:332px"><i></i>Lorem ipsum dolor sit amet, consectetur adipisci</div>
<div class="abs ribbon" style="top:363px"><i></i>Lorem ipsum dolor sit amet, consectetur adipisci</div>

<div class="abs enquire"></div>
<div class="abs enquire-head">Enquire Now for Training</div>
<div class="abs field" style="top:205px;height:19px">Name</div>
<div class="abs field" style="top:230px;height:19px">Email</div>
<div class="abs field" style="top:254px;height:20px">Phone</div>
<div class="abs field" style="top:279px;height:19px">Select Country<span style="float:right;color:#aaa">▾</span></div>
<div class="abs field" style="top:303px;height:39px;line-height:9px">Enter Course Detail and Preferred Month</div>
<div class="abs field" style="top:350px;height:16px;width:60px;padding:3px 9px">Enter Code</div>
<div class="abs captcha">B26SP</div>
<div class="abs btn" style="left:602px;top:374px;width:51px">Enquire</div>

<div class="abs intro-bar" style="left:78px"></div>
<h2 class="abs h2" style="left:90px;top:450px">WELCOME!</h2>
<p class="abs para" style="left:90px;top:478px">Aenean quis quam quis ipsum volutpat rutrum. Nam ultrices, tellus at viverra rutrum, massa nibkdf sh placerat est, a venenatis lorem neque et lectus. Nullam quis tortor sed nunc convallis blandit sed adfs urna. Vestibulum sit amet urna sit amet arcu venenatis commodo ac et ligula. Cras rutrum quam eget velit aliquam hendrerit. Mauris sed massa ligula. Suspendisse at velit ac eralop. dellop seelop daltersd sollicitudin interdum. Praesent vestibulum metus ac felis vehicula, at feugiat turpis pellentesque.ellop-er Nullam nec nunc accumsan, accumsan nibh vel, varius erat.</p>
<div class="abs btn" style="left:90px;top:558px;width:52px">Enquire</div>

<div class="abs intro-bar" style="left:430px"></div>
<h2 class="abs h2" style="left:442px;top:450px">ABOUT US</h2>
<p class="abs para" style="left:442px;top:478px">Aenean quis quam quis ipsum volutpat rutrum. Nam ultrices, tellus at viverra rutrum, massa nibkdf sh placerat est, a venenatis lorem neque et lectus. Nullam quis tortor sed nunc convallis blandit sed adfs urna. Vestibulum sit amet urna sit amet arcu venenatis commodo ac et ligula. Cras rutrum quam eget velit aliquam hendrerit. Mauris sed massa ligula. Suspendisse at velit ac eralop. dellop seelop daltersd sollicitudin interdum. Praesent vestibulum metus ac felis vehicula, at feugiat turpis pellentesque.ellop-er Nullam nec nunc accumsan, accumsan nibh vel, varius erat.</p>
<div class="abs btn" style="left:442px;top:558px;width:52px">Enquire</div>

<section class="abs band"></section>
<h2 class="abs h2" style="left:78px;top:616px">WHAT WE DO</h2>
<div class="abs what-item" style="top:649px"><div class="what-plus">+</div><div class="what-text">Nulla facilisi. Suspendisse gravida arcu eget iaculis accumsan. Sed pretium, felis at hendrerit porta, risus odio porta purus, eu viverra tortor turpis in erat. Integer hendrerit arcu quis eros bibendum,</div></div>
<div class="abs what-item" style="top:698px"><div class="what-plus">+</div><div class="what-text">Nulla facilisi. Suspendisse gravida arcu eget iaculis accumsan. Sed pretium, felis at hendrerit porta, risus odio porta purus, eu viverra tortor turpis in erat. Integer hendrerit arcu quis eros bibendum,</div></div>
<div class="abs what-item" style="top:748px"><div class="what-plus">+</div><div class="what-text">Nulla facilisi. Suspendisse gravida arcu eget iaculis accumsan. Sed pretium, felis at hendrerit porta, risus odio porta purus, eu viverra tortor turpis in erat. Integer hendrerit arcu quis eros bibendum,</div></div>
<div class="abs what-item" style="top:798px"><div class="what-plus">+</div><div class="what-text">Nulla facilisi. Suspendisse gravida arcu eget iaculis accumsan. Sed pretium, felis at hendrerit porta, risus odio porta purus, eu viverra tortor turpis in erat. Integer hendrerit arcu quis eros bibendum,</div></div>

<h2 class="abs h2" style="left:430px;top:617px">OUR SERVICING</h2>
<div class="abs serv-icon" style="left:431px;top:653px">
  <svg width="58" height="58" viewBox="0 0 58 58" fill="none" stroke="#222" stroke-width="2"><circle cx="24" cy="24" r="6"/><rect x="20" y="30" width="20" height="12"/><line x1="15" y1="44" x2="44" y2="44"/></svg>
</div>
<div class="abs serv-title" style="left:497px;top:657px">Yspendisse gravida arcu eget iaculis accumsan</div>
<p class="abs serv-text" style="left:496px;top:668px">Nulla facilisi. Suspendisse gravida arcu eget iaculis accumsan. Sed prpetium, felis alopt hendrerit porta, risus odio porta purus, eu viverra tortorlp turpis in erat. Integer hendrerit arcu quis eros bibendum,</p>

<div class="abs serv-icon" style="left:431px;top:717px">
  <svg width="58" height="58" viewBox="0 0 58 58" fill="none" stroke="#222" stroke-width="2"><circle cx="28" cy="28" r="13"/><ellipse cx="28" cy="28" rx="6" ry="13"/><line x1="15" y1="28" x2="41" y2="28"/></svg>
</div>
<div class="abs serv-title" style="left:497px;top:727px">Yspendisse gravida arcu eget iaculis accumsan</div>
<p class="abs serv-text" style="left:496px;top:738px">Nulla facilisi. Suspendisse gravida arcu eget iaculis accumsan. Sed prpetium, felis alopt hendrerit porta, risus odio porta purus, eu viverra tortorlp turpis in erat. Integer hendrerit arcu quis eros bibendum,</p>

<div class="abs serv-icon" style="left:431px;top:781px">
  <svg width="58" height="58" viewBox="0 0 58 58" fill="none" stroke="#222" stroke-width="2"><rect x="17" y="18" width="24" height="20" rx="2"/><line x1="22" y1="25" x2="36" y2="25"/><line x1="22" y1="31" x2="32" y2="31"/></svg>
</div>
<div class="abs serv-title" style="left:497px;top:792px">Yspendisse gravida arcu eget iaculis accumsan</div>
<p class="abs serv-text" style="left:496px;top:803px">Nulla facilisi. Suspendisse gravida arcu eget iaculis accumsan. Sed prpetium, felis alopt hendrerit porta, risus odio porta purus, eu viverra tortorlp turpis in erat. Integer hendrerit arcu quis eros bibendum,</p>

<svg class="abs" style="left:78px;top:917px" width="14" height="14" viewBox="0 0 14 14" fill="none" stroke="#444" stroke-width="1.2"><path d="M7 13C3 8 3 6 3 5a4 4 0 0 1 8 0c0 1 0 3-4 8z"/><circle cx="7" cy="5" r="1.5"/></svg>
<div class="abs contact-line" style="top:917px">USA – Riverton, 415 North K street, Lakeside, CA 90210</div>
<svg class="abs" style="left:78px;top:944px" width="14" height="12" viewBox="0 0 14 12" fill="none" stroke="#444" stroke-width="1.2"><rect x="1" y="2" width="12" height="8"/><path d="M1 2l6 5 6-5"/></svg>
<div class="abs contact-line link" style="left:105px;top:942px">demo link@t-o-m.example</div>
<svg class="abs" style="left:78px;top:970px" width="14" height="14" viewBox="0 0 14 14" fill="none" stroke="#444" stroke-width="1.2"><path d="M3 1l2 3-1 2c1 2 2 3 4 4l2-1 3 2-1 2C6 13 1 8 1 3z"/></svg>
<div class="abs contact-line link" style="left:105px;top:969px;line-height:13px">0800 555 0134<br>0800 555 0135</div>

<div class="abs quote-circle"></div>
<div class="abs quote-mark">“</div>
<div class="abs portrait" role="img" aria-label="Portrait photo of a grey-haired client giving a testimonial"></div>
<p class="abs testi">Nulla facilisi. Suspendisse gravida arcu eget iaculis accumsan. Sed pretium, felis at hendrerit porta, risus odio porta purus, eu viverra tortor turpis in erat. Integer hendrerit arcu quis eros biben-dum,ndisse gravida arcu eget iaculis accumsan. Sed pretium, felis at hendrerit porta, risus odio porta purus, eu viverra tortor turpis in erat. Integer hendrerit arcu quis eros bibendum, <b style="font-size:12px;color:#333">”</b></p>
<div class="abs testi-name">Yspendisse gravi</div>

<footer class="abs footer">
  <h3>GET IN TOUCH</h3>
  <p>Nulla facilisi. Suspendisse gravida arcu eget iaculis accumsan. Sed pretium, felis at hendrerit porta,<br>risus odio porta purus, eu viverra tortor turpis in erat. Integer hendrerit arcu quis eros bibendum,</p>
  <div class="socials"><span></span><span></span><span></span><span></span></div>
  <div class="fnav"><span>HOME</span><span>TRAINING</span><span>SERVICING</span><span>CONTACT</span></div>
  <div class="fbrand"><span class="brand-dot"></span><span class="brand-name">TOM Institute</span></div>
</footer>

</body>
</html>
```